We need a business card design for a Dubai based company .

We need a business card for a Dubai based company called "Marwaneq Smoking Requisites Trading LLC". We mainly import Flavoured Tobacco products and Charcoal which is used for smoking in a Hookah/Shisha and distribute to the wholesalers and retailers. Logo file is attached herewith.

```html
<!DOCTYPE html>
<html lang="en">
<head>
<meta charset="utf-8">
<title>Marwaneq Business Card</title>
<link href="https://fonts.googleapis.com/css2?family=Montserrat:wght@400;500;700&display=swap" rel="stylesheet">
<style>
  :root {
    --backdrop: #e4e4e2;
    --card-white: #ffffff;
    --brand-red: #b8282e;
    --ink-grey: #4a4a4a;
    --ink-dark: #1c1c1c;
  }
  * { margin: 0; padding: 0; box-sizing: border-box; }
  html, body { width: 1200px; height: 801px; overflow: hidden; }
  body {
    background: var(--backdrop);
    font-family: "Montserrat", sans-serif;
    display: flex;
    align-items: center;
    justify-content: center;
    gap: 40px;
  }
  .card {
    width: 530px;
    height: 303px;
    position: relative;
    box-shadow: 0 6px 18px rgba(0,0,0,0.12);
  }
  /* Front card */
  .card-front {
    background: var(--card-white);
    display: flex;
    align-items: center;
    border-bottom: 3px solid var(--brand-red);
  }
  .front-brand {
    width: 250px;
    display: flex;
    align-items: center;
    justify-content: center;
    padding-left: 26px;
  }
  .brand-name {
    font-weight: 700;
    color: var(--ink-dark);
    font-size: 13px;
    letter-spacing: 0.08em;
    line-height: 1.45;
    text-transform: uppercase;
  }
  .brand-mark {
    width: 14px; height: 14px;
    border: 2px solid var(--brand-red);
    margin-right: 12px;
    flex: none;
  }
  .divider {
    width: 1px;
    height: 150px;
    background: var(--brand-red);
    margin: 0 24px 0 12px;
  }
  .contact-block { color: var(--ink-grey); font-size: 13px; line-height: 1.5; }
  .person-name { color: var(--brand-red); font-weight: 700; font-size: 19px; letter-spacing: 0.01em; line-height: 1.1; }
  .person-role { font-size: 13px; margin-bottom: 14px; }
  .address { margin-bottom: 12px; }
  .contact-line { display: flex; align-items: center; gap: 8px; }
  .contact-line svg { width: 11px; height: 11px; fill: var(--brand-red); flex: none; }
  /* Back card */
  .card-back {
    background: var(--brand-red);
    display: flex;
    align-items: center;
    justify-content: center;
  }
  .back-brand {
    display: flex;
    align-items: center;
  }
  .back-brand .brand-name {
    color: var(--card-white);
    font-size: 17px;
    letter-spacing: 0.12em;
    line-height: 1.5;
  }
  .back-brand .brand-mark { border-color: var(--card-white); width: 18px; height: 18px; margin-right: 16px; }
</style>
</head>
<body>
  <section class="card card-front">
    <div class="front-brand">
      <span class="brand-mark"></span>
      <p class="brand-name">Marwaneq<br>Smoking Requisites<br>Trading LLC</p>
    </div>
    <div class="divider"></div>
    <div class="contact-block">
      <p class="person-name">SAM CORLAN</p>
      <p class="person-role">President</p>
      <p class="address">18240 Harbor View Dr<br>Laguna Point CA 92611</p>
      <p class="contact-line">
        <svg viewBox="0 0 24 24"><path d="M6.6 10.8a15.1 15.1 0 0 0 6.6 6.6l2.2-2.2a1 1 0 0 1 1-.25 11.4 11.4 0 0 0 3.6.57 1 1 0 0 1 1 1V20a1 1 0 0 1-1 1A17 17 0 0 1 3 4a1 1 0 0 1 1-1h3.5a1 1 0 0 1 1 1c0 1.25.2 2.45.57 3.57a1 1 0 0 1-.25 1z"/></svg>
        949-555-0187
      </p>
      <p class="contact-line">
        <svg viewBox="0 0 24 24"><path d="M2 5h20v14H2z M2 5l10 8 10-8" /></svg>
        sam@marwaneq.com
      </p>
      <p class="contact-line">
        <svg viewBox="0 0 24 24"><circle cx="12" cy="12" r="10"/></svg>
        www.marwaneq.com
      </p>
    </div>
  </section>

  <section class="card card-back">
    <div class="back-brand">
      <span class="brand-mark"></span>
      <p class="brand-name">Marwaneq<br>Smoking Requisites<br>Trading LLC</p>
    </div>
  </section>
</body>
</html>
```